Flyer Design Project for lawn care business

I need a flyer designed for my lawn care business, "Ashby's Groundcare Services".  It is a family owned small landscaping company. I was thinking something that I can print  2- 3 per page.
I have  2 different logos I can upload to give an idea.  I have seen some I like that are colorfull with neat graphics but I also like some that are simple and elegant.  I would like something that catches your eye and looks professionaly done.

Target Market(s)
Homeowners in Durham, North Carolina with homes usually valued $200,000 or more.
Industry/Entity Type
Landscaping
Requirements
Must have
- I would like the address of my website listed on it, www.ashbygroundcareservices.com
I would like for it to say somewhere, 50% off first service with seasonal service.
Not sure if I want to list some of the services that I offer or just say full service lawn care.
Nice to have
- I have a logo with a bull pushing a lawn mower.  I live in Durham, NC also known as the Bull City.  I am not in love with the logo so feel free to change it or not use it at all.

```html
<!DOCTYPE html>
<html lang="en">
<head>
<meta charset="utf-8">
<title>Ashby's Groundcare Services – Flyer</title>
<link rel="stylesheet" href="https://fonts.googleapis.com/css2?family=Archivo+Black&family=Fondamento&family=Cabin:wght@400&family=Oswald:wght@600&display=swap">
<style>
  :root {
    --bg-top: #ededed;
    --bg-mid: #a9a9a9;
    --bg-bottom: #262626;
    --brand-orange: #ee6f0c;
    --wave-blue: #a4dbea;
    --ink: #111111;
    --white: #ffffff;
    --url-red: #e3161b;
    --leaf-green: #2f8a2a;
    --mark-green: #6cae2d;
  }
  * { margin: 0; padding: 0; box-sizing: border-box; }
  html, body { width: 1200px; height: 2590px; overflow: hidden; background: var(--bg-bottom); }
  .flyer {
    position: relative;
    width: 1200px;
    height: 2590px;
    overflow: hidden;
    background: linear-gradient(to bottom, var(--bg-top) 0%, #dcdcdc 25%, var(--bg-mid) 55%, #4a4a4a 80%, var(--bg-bottom) 100%);
  }
  .brand-dot {
    position: absolute;
    left: 45px; top: 150px;
    width: 250px; height: 250px;
    border-radius: 50%;
    background: var(--leaf-green);
  }
  .brand-name {
    position: absolute;
    right: 40px; top: 330px;
    text-align: right;
    font-family: "Archivo Black", "Arial Black", sans-serif;
    color: var(--brand-orange);
    line-height: 1;
  }
  .brand-name .line-1 { display: block; font-size: 118px; }
  .brand-name .line-2 { display: block; font-size: 72px; margin-top: 22px; }
  .mower-area {
    position: absolute;
    left: 30px; top: 1390px;
    width: 1170px; height: 1060px;
    background: radial-gradient(ellipse at 60% 50%, rgba(70,70,70,0.55) 0%, rgba(60,60,60,0.25) 55%, rgba(60,60,60,0) 75%);
  }
  .wave {
    position: absolute;
    left: 0; top: 0;
    width: 1200px; height: 2590px;
  }
  .offer {
    position: absolute;
    left: 100px; top: 1050px;
    font-family: "Fondamento", "Georgia", serif;
    font-size: 108px;
    letter-spacing: -4px;
    line-height: 200px;
    color: var(--ink);
    text-shadow: 4px 5px 6px rgba(0,0,0,0.35);
  }
  .offer span { display: block; }
  .offer .line-2 { margin-left: -20px; }
  .tagline {
    position: absolute;
    left: 32px; top: 2305px;
    font-family: "Cabin", "Trebuchet MS", sans-serif;
    font-size: 80px;
    color: var(--white);
  }
  .corner-mark {
    position: absolute;
    left: 925px; top: 2195px;
    width: 200px; height: 200px;
    background: var(--mark-green);
  }
  .web-address {
    position: absolute;
    left: 0; width: 1200px; top: 2440px;
    text-align: center;
    font-family: "Oswald", "Arial Narrow", sans-serif;
    font-weight: 600;
    font-size: 84px;
    letter-spacing: -1px;
    color: var(--url-red);
    text-shadow: 2px 2px 0 rgba(255,255,255,0.35);
  }
</style>
</head>
<body>
  <main class="flyer">
    <header class="brand">
      <div class="brand-dot"></div>
      <h1 class="brand-name">
        <span class="line-1">ASHBY'S</span>
        <span class="line-2">GROUNDCARE SERVICES</span>
      </h1>
    </header>

    <div class="mower-area" role="img" aria-label="Faint illustration of a push lawn mower"></div>

    <svg class="wave" viewBox="0 0 1200 2590" aria-hidden="true">
      <path fill="var(--wave-blue)" d="M0,950 C250,880 600,960 850,860 C1000,800 1100,760 1160,720 C1170,900 1120,1200 980,1320 C880,1410 760,1450 600,1480 C380,1520 220,1620 170,1760 C150,1850 140,1920 120,1980 L0,1990 Z"/>
    </svg>

    <p class="offer">
      <span class="line-1">50% off first service</span>
      <span class="line-2">with seasonal service.</span>
    </p>

    <p class="tagline">Full Service Lawn Care.</p>
    <div class="corner-mark"></div>
    <p class="web-address">www.ashbygroundcareservices.com</p>
  </main>
</body>
</html>
```